"Breathe & Bloom" Book Cover 5.5x8.5

Title of the book is "Breathe & Bloom"
Subtitle is "Unmasking Pricing Myths"
I've used PixelGuild on multiple occasions you can look on my Borvex page, Mark Delwitt, to see the covers I've used in the other projects I've done.
The target audience are people who have been tricked to think they can't retire because inflation, i.e. cost of living is going up so much they must work to keep up. There is no evidence of this.
And those are the people I want to reach so they can "Breathe...and Bloom."
Target Market(s)
Americans aged 55 and over who are thinking about retirement
Industry/Entity Type
Financial
Requirements
Nice to have
- Keep It Simple, Stupid is my mantra. Just make it pop out when people are browsing
Should not have
- No piggy banks. No old people sitting on a beach.

```html
<!DOCTYPE html>
<html lang="en">
<head>
<meta charset="utf-8">
<title>Breathe &amp; Bloom — Book Cover</title>
<link rel="stylesheet" href="https://fonts.googleapis.com/css2?family=Josefin+Sans:wght@300;400&family=Julius+Sans+One&family=Questrial&display=swap">
<style>
  :root {
    --sky-top: #e4dfe9;
    --sky-mid: #f1eef2;
    --haze: #fbf9fa;
    --sea: #f3efef;
    --surf: #e9dcdc;
    --sand: #dcc4bf;
    --sand-deep: #d6bab4;
    --title-pale: #f1eff4;
    --title-blue: #62b2d8;
    --title-gray: #7f7f82;
    --amp: #b9adae;
    --rule: #5a5a5a;
    --author-light: #cfcacc;
    --author-dark: #808082;
    --subtitle: #ffffff;
    --band: rgba(255, 255, 255, 0.38);
  }
  * { margin: 0; padding: 0; box-sizing: border-box; }
  html, body { width: 750px; height: 1200px; overflow: hidden; background: var(--haze); }
  .cover { position: relative; width: 750px; height: 1200px; overflow: hidden; }
  .cover-scene {
    position: absolute; inset: 0;
    background: linear-gradient(180deg,
      var(--sky-top) 0%,
      var(--sky-mid) 30%,
      var(--haze) 50%,
      var(--haze) 58%,
      var(--sea) 64%,
      var(--surf) 72%,
      #e6d6d4 78%,
      var(--sand) 86%,
      var(--sand-deep) 100%);
  }
  .author-band {
    position: absolute; left: 0; top: 592px; width: 750px; height: 138px;
    background: var(--band);
  }
  .cover-type { position: absolute; inset: 0; }
  .title-word { font-family: 'Josefin Sans', sans-serif; font-weight: 400; font-size: 112px; }
  .ampersand { font-family: 'Josefin Sans', sans-serif; font-weight: 300; font-size: 44px; fill: var(--amp); }
  .title-rule { stroke: var(--rule); stroke-width: 0.6; }
  .author { font-family: 'Julius Sans One', sans-serif; font-size: 30px; }
  .author .initial { font-size: 40px; }
  .subtitle { font-family: 'Questrial', sans-serif; font-size: 40px; fill: var(--subtitle); opacity: 0.92; }
</style>
</head>
<body>
<main class="cover">
  <div class="cover-scene" role="img" aria-label="Soft pastel photograph of a hazy sky over the ocean, with waves breaking onto a pink sandy beach"></div>
  <div class="author-band"></div>

  <svg class="cover-type" width="750" height="1200" viewBox="0 0 750 1200" xmlns="http://www.w3.org/2000/svg">
    <defs>
      <linearGradient id="top-word-fill" gradientUnits="userSpaceOnUse" x1="100" y1="0" x2="650" y2="0">
        <stop offset="0.15" stop-color="var(--title-pale)"/>
        <stop offset="0.35" stop-color="#cde6f1"/>
        <stop offset="1" stop-color="var(--title-blue)"/>
      </linearGradient>
      <linearGradient id="bottom-word-fill" gradientUnits="userSpaceOnUse" x1="70" y1="0" x2="685" y2="0">
        <stop offset="0.45" stop-color="var(--title-pale)"/>
        <stop offset="0.6" stop-color="#d9d9db"/>
        <stop offset="1" stop-color="var(--title-gray)"/>
      </linearGradient>
      <linearGradient id="author-fill" gradientUnits="userSpaceOnUse" x1="220" y1="0" x2="530" y2="0">
        <stop offset="0" stop-color="var(--author-light)"/>
        <stop offset="0.4" stop-color="var(--author-dark)"/>
        <stop offset="1" stop-color="var(--author-dark)"/>
      </linearGradient>
    </defs>

    <text class="title-word" x="100" y="205" textLength="550" lengthAdjust="spacing" fill="url(#top-word-fill)">BREATHE</text>

    <line class="title-rule" x1="280" y1="277" x2="470" y2="277"/>
    <text class="ampersand" x="375" y="290" text-anchor="middle">&amp;</text>

    <text class="title-word" x="70" y="467" textLength="615" lengthAdjust="spacing" fill="url(#bottom-word-fill)">BLOOM</text>

    <text class="author" x="375" y="688" text-anchor="middle" fill="url(#author-fill)"><tspan class="initial">M</tspan>ARK <tspan class="initial">D</tspan>ELWITT</text>

    <text class="subtitle" x="50" y="1055" textLength="655" lengthAdjust="spacing">UNMASKING PRICING MYTHS</text>
  </svg>
</main>
</body>
</html>
```